Tamarack Hearth Partners Business Card

Looking for a new business card layout. We are a real estate firm w/ a logo, old design attached. Must keep the same elements on there, just need a fresh look and possible some foil accents. Looking for a simpler design w/ more modern style.

Target Market(s)

Real Estate clients

Industry/Entity Type

Real Estate Agent

Contact Information for Business Card

see attached

Font styles to use
Sans Serif

Requirements
Must have
• all elements on current biz card
Nice to have
• modern look, simpler than we have!
Should not have
• no serif fonts

```html
<!DOCTYPE html>
<html lang="en">
<head>
<meta charset="utf-8">
<title>Tamarack Hearth Partners Business Card</title>
<link href="https://fonts.googleapis.com/css2?family=Nunito+Sans:wght@300;400;700;800&display=swap" rel="stylesheet">
<style>
  :root {
    --backdrop: #d6d7d6;
    --card: #0b0b0b;
    --gold: #c4922f;
    --gold-light: #d9ad5a;
    --white: #ffffff;
    --photo-top: #e9e4de;
    --photo-mid: #c8b79a;
    --photo-low: #34c2c4;
  }
  * { box-sizing: border-box; margin: 0; padding: 0; }
  html, body { width: 1200px; height: 900px; overflow: hidden; }
  body {
    background: var(--backdrop);
    font-family: "Nunito Sans", sans-serif;
    color: var(--white);
    position: relative;
  }
  .card {
    position: absolute;
    left: 250px;
    width: 700px;
    height: 400px;
    background: var(--card);
    overflow: hidden;
    box-shadow: 0 6px 18px rgba(0,0,0,0.18);
  }
  .card--back { top: 30px; }
  .card--front { top: 470px; }

  .wordmark {
    color: var(--gold);
    font-weight: 800;
    text-transform: uppercase;
    line-height: 0.95;
    letter-spacing: 0.01em;
  }
  .card--back .wordmark {
    position: absolute;
    left: 150px;
    top: 110px;
    font-size: 52px;
  }

  .gold-band {
    position: absolute;
    left: 0;
    width: 100%;
    height: 22px;
    background: var(--gold);
  }
  .card--back .gold-band { top: 340px; }

  .web {
    position: absolute;
    font-size: 17px;
    font-weight: 400;
    color: var(--white);
  }
  .web strong { font-weight: 800; }
  .card--back .web { left: 30px; top: 312px; }

  /* front */
  .card--front .wordmark {
    position: absolute;
    left: 34px;
    top: 30px;
    font-size: 34px;
  }
  .agent {
    position: absolute;
    left: 34px;
    top: 118px;
  }
  .agent-name {
    color: var(--gold);
    font-size: 28px;
    font-weight: 800;
    text-transform: uppercase;
    line-height: 1;
  }
  .agent-title {
    font-size: 15px;
    font-weight: 400;
    margin-top: 4px;
  }
  .contact {
    position: absolute;
    left: 34px;
    top: 196px;
    font-size: 15px;
    font-weight: 400;
    line-height: 1.35;
  }
  .phone {
    display: flex;
    align-items: center;
    gap: 8px;
    font-size: 24px;
    font-weight: 800;
    line-height: 1.2;
  }
  .phone svg { width: 18px; height: 18px; flex: none; }
  .email { font-size: 18px; font-weight: 300; margin-top: 2px; }
  .address { margin-bottom: 6px; }

  .portrait {
    position: absolute;
    right: 0;
    top: 0;
    width: 300px;
    height: 318px;
    background: linear-gradient(180deg, var(--photo-top) 0%, var(--photo-mid) 55%, var(--photo-low) 100%);
  }
  .card--front .gold-band { top: 318px; left: 400px; width: 300px; height: 20px; }
  .card--front .web { left: 34px; top: 360px; }
  .card--front .bottom-rule {
    position: absolute;
    left: 0; top: 386px;
    width: 100%; height: 14px;
    background: var(--gold);
  }
</style>
</head>
<body>

  <section class="card card--back" aria-label="Card back">
    <div class="wordmark">Tamarack Hearth<br>Partners</div>
    <p class="web">www.<strong>TamarackHearth-Homes</strong>.com</p>
    <div class="gold-band"></div>
  </section>

  <section class="card card--front" aria-label="Card front">
    <div class="wordmark">Tamarack Hearth<br>Partners</div>

    <div class="agent">
      <p class="agent-name">Dana Whitfield</p>
      <p class="agent-title">Principal Broker</p>
    </div>

    <div class="contact">
      <p class="address">482 NW Birch Ave, Sisters, OR 97759</p>
      <p class="phone">
        <svg viewBox="0 0 24 24" aria-hidden="true"><path fill="#c4922f" d="M6.6 10.8c1.4 2.8 3.8 5.1 6.6 6.6l2.2-2.2c.3-.3.7-.4 1-.2 1.1.4 2.3.6 3.6.6.6 0 1 .4 1 1V20c0 .6-.4 1-1 1C10.6 21 3 13.4 3 4c0-.6.4-1 1-1h3.5c.6 0 1 .4 1 1 0 1.3.2 2.5.6 3.6.1.3 0 .7-.2 1z"/></svg>
        555.204.3187
      </p>
      <p class="phone">
        <svg viewBox="0 0 24 24" aria-hidden="true"><rect x="6" y="2" width="12" height="20" rx="2" fill="none" stroke="#c4922f" stroke-width="2"/><circle cx="12" cy="18" r="1.2" fill="#c4922f"/></svg>
        555.318.6042
      </p>
      <p class="email">dana@tamarackhearth.com</p>
    </div>

    <div class="portrait" role="img" aria-label="Portrait photo of the broker"></div>
    <div class="gold-band"></div>

    <p class="web">www.<strong>TamarackHearth-Homes</strong>.com</p>
    <div class="bottom-rule"></div>
  </section>

</body>
</html>
```